Pharmacy window design

WINDOW DIMENSIONS

4ft 8 1/2" WIDE
7ft 4 1/2" HIGH

i need a window sticker for 4 windows for the outside of a pharmacy. see attached examples. name of the pharmacy is Vita Corner

we would prefer to display products on the window signs eg. Baby care products, medicines. vitamins. fitness. veterinary, Health/ beauty etc.

Target Market(s)

Locals and Tourists

Industry/Entity Type

Pharmacy

```html
<!DOCTYPE html>
<html lang="en">
<head>
<meta charset="utf-8">
<title>Vita Corner Pharmacy – Window Sign</title>
<link rel="stylesheet" href="https://fonts.googleapis.com/css2?family=Arimo:wght@400;700&display=swap">
<style>
  :root {
    --brand-blue: #1f6fc4;
    --brand-green: #5db535;
    --band-green: #64b83a;
    --white: #ffffff;
    --panel-grey: #e9ecef;
    --hours-blue: #1d5fae;
    --capsule-blue: #2a66c9;
    --capsule-deep: #1c4fa8;
    --capsule-light: #f4f6f8;
  }
  * { margin: 0; padding: 0; box-sizing: border-box; }
  html, body {
    width: 800px;
    height: 1200px;
    overflow: hidden;
    background: var(--white);
    font-family: "Arimo", Arial, sans-serif;
  }
  .window-sign {
    position: relative;
    width: 800px;
    height: 1200px;
    display: flex;
    flex-direction: column;
    background: var(--panel-grey);
  }
  .brand-header {
    height: 390px;
    background: var(--white);
    display: flex;
    align-items: center;
    justify-content: center;
    gap: 30px;
    padding-bottom: 20px;
  }
  .brand-dot {
    width: 120px;
    height: 120px;
    border-radius: 50%;
    background: var(--brand-green);
    flex-shrink: 0;
  }
  .brand-text { display: flex; flex-direction: column; }
  .brand-name {
    font-size: 82px;
    font-weight: 700;
    color: var(--brand-blue);
    line-height: 1;
    letter-spacing: -1px;
  }
  .brand-type {
    margin-top: 12px;
    font-size: 34px;
    font-weight: 700;
    color: var(--brand-green);
    letter-spacing: 3px;
  }
  .brand-phone {
    margin-top: 8px;
    font-size: 22px;
    font-weight: 700;
    color: var(--brand-blue);
    letter-spacing: 1px;
  }
  .opening-band {
    height: 130px;
    background: var(--band-green);
    display: flex;
    align-items: center;
    justify-content: center;
  }
  .opening-band h2 {
    color: var(--white);
    font-size: 62px;
    font-weight: 700;
    letter-spacing: 0.5px;
    white-space: nowrap;
  }
  .opening-hours {
    height: 260px;
    padding: 55px 0 0 70px;
    color: var(--hours-blue);
    font-size: 54px;
    font-weight: 700;
  }
  .hours-row { display: flex; line-height: 1.4; white-space: nowrap; }
  .hours-day { width: 300px; }
  .hours-row.sunday .hours-time { padding-left: 30px; }
  .product-visual {
    flex: 1;
    margin: 0 0 40px;
    background:
      radial-gradient(ellipse 70% 60% at 40% 50%, var(--capsule-deep) 0%, var(--capsule-blue) 40%, rgba(42,102,201,0.45) 70%, rgba(244,246,248,0) 100%),
      linear-gradient(180deg, var(--panel-grey) 0%, var(--capsule-light) 100%);
  }
</style>
</head>
<body>
  <main class="window-sign">
    <header class="brand-header">
      <div class="brand-dot"></div>
      <div class="brand-text">
        <h1 class="brand-name">Vita Corner</h1>
        <span class="brand-type">PHARMACY</span>
        <span class="brand-phone">TEL: 020 555 0148</span>
      </div>
    </header>

    <section class="opening-band">
      <h2>OPEN 7 DAYS A WEEK</h2>
    </section>

    <section class="opening-hours">
      <div class="hours-row">
        <span class="hours-day">Mon-Sat :</span>
        <span class="hours-time">8:30am-7pm</span>
      </div>
      <div class="hours-row sunday">
        <span class="hours-day">Sun :</span>
        <span class="hours-time">10am-2pm</span>
      </div>
    </section>

    <div class="product-visual" role="img" aria-label="Product photograph: a pile of blue and white medicine capsules"></div>
  </main>
</body>
</html>
```